Business Card Designs

Looking to design a 3.5" x 2" standard business card for our employees.
The design needs to be sleek, simple, and modern. We would like our logo (attached) to be incorporated, but not in that colour, rather an outline of the logo in either gold or silver (whichever looks better).

Modern and Simple is what we are looking for, but be creative in incorporating the logo.

```html
<!DOCTYPE html>
<html lang="en">
<head>
<meta charset="UTF-8">
<title>Halden Suite Residences – Business Card</title>
<link href="https://fonts.googleapis.com/css2?family=Bebas+Neue&family=Oswald:wght@400;500&display=swap" rel="stylesheet">
<style>
  :root {
    --backdrop: #c8c8c8;
    --card: #050505;
    --gold: #c9a133;
    --gold-deep: #9c7a22;
    --gold-light: #e0bd55;
  }
  * { margin: 0; padding: 0; box-sizing: border-box; }
  html, body { width: 900px; height: 1200px; overflow: hidden; }
  body {
    background: var(--backdrop);
    position: relative;
    font-family: "Oswald", sans-serif;
    color: var(--gold);
  }
  .card {
    position: absolute;
    top: 495px;
    width: 369px;
    height: 210px;
    background: var(--card);
    overflow: hidden;
  }
  .card--front { left: 60px; }
  .card--back { left: 471px; }

  .accent-band {
    position: absolute;
    left: 0; right: 0;
    top: 158px;
    height: 12px;
    background: linear-gradient(90deg, var(--gold-deep), var(--gold-light) 50%, var(--gold-deep));
  }

  .brand-mark {
    position: absolute;
    display: flex;
    align-items: center;
    gap: 5px;
    font-family: "Bebas Neue", sans-serif;
    color: var(--gold);
    letter-spacing: 0.06em;
    line-height: 1;
  }
  .brand-mark__square {
    width: 9px; height: 9px;
    border: 1.2px solid var(--gold);
  }
  .card--front .brand-mark { left: 30px; top: 34px; font-size: 15px; }
  .card--back .brand-mark { left: 30px; top: 22px; font-size: 10px; }

  .website {
    position: absolute;
    left: 0; right: 0;
    top: 188px;
    text-align: center;
    font-size: 7px;
    letter-spacing: 0.2em;
    text-transform: uppercase;
    display: flex;
    justify-content: center;
    align-items: center;
    gap: 5px;
  }

  .company-name {
    position: absolute;
    left: 0; right: 0;
    top: 60px;
    text-align: center;
    font-family: "Bebas Neue", sans-serif;
    font-size: 22px;
    letter-spacing: 0.02em;
    line-height: 1;
  }
  .address {
    position: absolute;
    left: 0; right: 0;
    top: 84px;
    display: flex;
    justify-content: center;
    align-items: center;
    gap: 4px;
    font-size: 5.5px;
    letter-spacing: 0.12em;
    text-transform: uppercase;
  }
  .contact-row {
    position: absolute;
    left: 0; right: 0;
    top: 123px;
    display: flex;
    justify-content: center;
    align-items: center;
    gap: 5px;
    font-size: 6px;
    letter-spacing: 0.14em;
    text-transform: uppercase;
  }
  .contact-item { display: flex; align-items: center; gap: 4px; }
  .divider { width: 1px; height: 10px; background: var(--gold); }
  .icon { width: 7px; height: 7px; fill: var(--gold); flex: none; }
</style>
</head>
<body>

  <section class="card card--front">
    <div class="brand-mark">
      <span class="brand-mark__square"></span>
      <span>Halden Suite Residences</span>
    </div>
    <div class="accent-band" role="img" aria-label="Gold diagonal-striped accent band"></div>
    <p class="website">www.haldensuiteresidences.com</p>
  </section>

  <section class="card card--back">
    <div class="brand-mark">
      <span class="brand-mark__square"></span>
      <span>Halden Suite Residences</span>
    </div>

    <h1 class="company-name">Halden Suite Residences</h1>

    <p class="address">
      <svg class="icon" viewBox="0 0 10 10" aria-hidden="true">
        <path d="M5 0C3 0 1.6 1.5 1.6 3.4 1.6 6 5 10 5 10s3.4-4 3.4-6.6C8.4 1.5 7 0 5 0zm0 4.8a1.4 1.4 0 1 1 0-2.8 1.4 1.4 0 0 1 0 2.8z"/>
      </svg>
      42 Marlow Ave, Suite 310 Halden, ON K2P 4B8
    </p>

    <div class="contact-row">
      <span class="contact-item">
        <svg class="icon" viewBox="0 0 10 10" aria-hidden="true">
          <path d="M2.2 0.5l1.6 2-1 1.2c.6 1.4 1.7 2.5 3.1 3.1l1.2-1 2 1.6-.9 1.7C4.4 9 1 5.6.5 1.4z"/>
        </svg>
        (555) 014-2231
      </span>
      <span class="divider"></span>
      <span class="contact-item">
        <svg class="icon" viewBox="0 0 10 10" aria-hidden="true">
          <path d="M2.2 0.5l1.6 2-1 1.2c.6 1.4 1.7 2.5 3.1 3.1l1.2-1 2 1.6-.9 1.7C4.4 9 1 5.6.5 1.4z"/>
        </svg>
        (555) 019-7740
      </span>
      <span class="divider"></span>
      <span class="contact-item">
        <svg class="icon" viewBox="0 0 10 10" aria-hidden="true">
          <path d="M0 2h10v6H0z M0 2l5 3.4L10 2" fill="none" stroke="currentColor"/>
          <path d="M0 2h10L5 5.6z"/>
        </svg>
        info@haldensuiteresidences.com
      </span>
    </div>

    <div class="accent-band" role="img" aria-label="Gold diagonal-striped accent band"></div>

    <p class="website">
      <svg class="icon" viewBox="0 0 10 10" aria-hidden="true">
        <circle cx="5" cy="5" r="4.3" fill="none" stroke="#c9a133" stroke-width="1"/>
        <path d="M0.7 5h8.6M5 0.7c-2 2.4-2 6.2 0 8.6M5 0.7c2 2.4 2 6.2 0 8.6" fill="none" stroke="#c9a133" stroke-width="0.8"/>
      </svg>
      www.haldensuiteresidences.com
    </p>
  </section>

</body>
</html>
```